Etiketten-Design für eingekochte Erzeugnisse
Zielgruppe
Wir sind ein regional tätiger Cateringbetrieb und Hersteller von hausgemachten, qualitativ hochwertigen Saucen, Suppen und Dips. Für unsere eingekochten Erzeugnisse suchen wir ein Etikett für durchsichtige Gläser (327 ml, TO 66) mit kupferfarbenem Twist-Off-Deep Verschluss. Da es sich um hochwertige Produkte handelt, sollte dies auch das Etikett widerspiegeln und nicht „billig“ aussehen. Das Design sollte modern, hip und farblich zum Kupferdeckel passen.
Aufgabenstellung
Das Etikett sollte über den gesamten Umfang des Glases gehen. Als Endformat stellen wir uns eine Breite des Etiketts von 220 mm und eine Höhe von 90 mm vor.
Da wir unterschiedliche Sorten anbieten, sollten sich diese in den Etiketten wiederfinden. Jede Sorte sollte also ein individuell auf den Inhalt angepasstes Etikett haben. Zudem sollte das Etikett später auch anpassbar sein, da sich die Vorschriften zur Deklaration sowie die Zutatenliste ändern können. Die Grammangabe der Gesamtmenge sollte ebenfalls anpassbar sein können.
Für unsere Marke „Topfzauber“ suchen wir außerdem ein neues Wort-Bild-Logo,
welches gleich auf dem Etikett platziert werden soll. Das Logo sollte also in das Etikett eingefügt sein, aber auch für die Homepage und den Rechnungsbogen geeignet sein.
Unser Sortiment umfasst die Saucensorten:
- Tomatensauce
- Bratensauce
- Rahmsauce
- Bolognesesauce
- Chilli con Carne
- Linsenbolognese, vegetarisch
- Gelbes Thai Curry, vegetarisch
- Ungarische Gulaschsuppe
- Karibischer Süßkartoffel-Kürbis Eintopf
- Indischer Linsencurry
Was soll auf das Etikett:
Saucen Sorte (Bezeichnung)
Hersteller:
Partyservice Hellwanger
Markus Hellwanger
Lerchenfeld 9
88999 Beispielstadt
Inhalt:
360g
Zutaten:
Anpassbares Zutatentextfeld
Anpassbare Nährwerttabelle mit den Big 7
Haltbarkeit:
Mindestens haltbar bis: siehe Deckel
Hinweise:
Kann Spuren von Sellerie und Nüssen enthalten.
Kühl, trocken und lichtgeschützt lagern.
Nach dem Öffnen im Kühlschrank aufbewahren und innerhalb weniger Tage aufbrauchen.
Weiße Fläche freihalten, um später eventuell einen Barcode einzufügen.
Internetadresse:
www.topfzauber-beispiel.de

```html
<!DOCTYPE html>
<html lang="de">
<head>
<meta charset="utf-8">
<title>Topfzauber – Etiketten</title>
<link rel="stylesheet" href="https://fonts.googleapis.com/css2?family=Amatic+SC:wght@700&family=Pathway+Gothic+One&display=swap">
<style>
  :root {
    --canvas: #ffffff;
    --label-white: #ffffff;
    --ink: #3b302c;
    --logo-disc: #1d1b1b;
    --logo-text: #ffffff;
    --tomato-panel: #eda397;
    --tomato-title: #c8262b;
    --tomato-art-a: #e8826f;
    --tomato-art-b: #f3e6e4;
    --mushroom-panel: #d5ab79;
    --mushroom-title: #6c4a4c;
    --mushroom-art-a: #a08463;
    --mushroom-art-b: #d9cdb6;
    --chili-panel: #97c0a4;
    --chili-title: #c8262b;
    --chili-art-a: #d64a3d;
    --chili-art-b: #7fae7c;
  }
  html, body {
    margin: 0;
    padding: 0;
    width: 1200px;
    height: 916px;
    overflow: hidden;
    background: var(--canvas);
  }
  .label-row {
    position: relative;
    width: 1200px;
    height: 916px;
  }
  .label {
    position: absolute;
    top: 129px;
    width: 368px;
    height: 486px;
  }
  .label--tomato   { left: 18px;  --panel: var(--tomato-panel);   --title: var(--tomato-title);   --art-a: var(--tomato-art-a);   --art-b: var(--tomato-art-b); }
  .label--mushroom { left: 417px; --panel: var(--mushroom-panel); --title: var(--mushroom-title); --art-a: var(--mushroom-art-a); --art-b: var(--mushroom-art-b); }
  .label--chili    { left: 816px; --panel: var(--chili-panel);    --title: var(--chili-title);    --art-a: var(--chili-art-a);    --art-b: var(--chili-art-b); }

  .label__tab {
    position: absolute;
    left: 143px;
    top: 0;
    width: 62px;
    height: 212px;
    background: var(--panel);
  }
  .label__band {
    position: absolute;
    left: 0;
    top: 211px;
    width: 368px;
    height: 275px;
    background: var(--label-white);
    overflow: hidden;
  }
  .label__art {
    position: absolute;
    left: 0;
    top: 60px;
    width: 230px;
    height: 215px;
    background: radial-gradient(ellipse at 35% 45%, var(--art-a) 0%, var(--art-b) 55%, var(--label-white) 85%);
  }
  .label__panel {
    position: absolute;
    left: 0;
    top: 0;
    width: 368px;
    height: 275px;
  }
  .label__panel path { fill: var(--panel); }

  .label__text {
    position: absolute;
    left: 118px;
    width: 250px;
    top: 50px;
    text-align: center;
    color: var(--ink);
  }
  .label__title {
    margin: 0;
    font-family: "Amatic SC", cursive;
    font-weight: 700;
    font-size: 40px;
    line-height: 1;
    letter-spacing: 0.5px;
    color: var(--title);
  }
  .label__title small {
    font-size: 30px;
    text-transform: lowercase;
  }
  .label__claim {
    margin: 10px 0 0;
    font-family: "Pathway Gothic One", sans-serif;
    font-size: 15px;
    line-height: 21px;
    letter-spacing: 0.4px;
  }
  .label__claim--mixed { letter-spacing: 0.6px; }
  .label__amount {
    margin: 14px 0 0;
    font-family: "Pathway Gothic One", sans-serif;
    line-height: 1;
  }
  .label__amount-key { font-size: 10px; }
  .label__amount-value { font-size: 27px; }
  .label__portions {
    display: block;
    font-size: 10px;
    margin-top: 2px;
  }

  .brand-mark {
    position: absolute;
    left: 118px;
    top: 158px;
    width: 106px;
    height: 106px;
    border-radius: 50%;
    background: var(--logo-disc);
    display: flex;
    align-items: center;
    justify-content: center;
    font-family: "Amatic SC", cursive;
    font-weight: 700;
    font-size: 24px;
    color: var(--logo-text);
  }
</style>
</head>
<body>
<main class="label-row">

  <section class="label label--tomato">
    <div class="label__tab"></div>
    <div class="label__band">
      <div class="label__art" role="img" aria-label="Aquarell-Illustration: Tomaten, Knoblauch und Pfefferkörner"></div>
      <svg class="label__panel" viewBox="0 0 368 275" aria-hidden="true">
        <path d="M96 0 C 96 150 175 255 292 275 L368 275 L368 0 Z"/>
      </svg>
      <div class="label__text">
        <h2 class="label__title">Tomatensauce</h2>
        <p class="label__claim">VOLLREIFE AROMATISCHE TOMATEN<br>UND MEDITERRANE GEWÜRZE</p>
        <p class="label__amount"><span class="label__amount-key">Inhalt</span> <span class="label__amount-value">360g</span><span class="label__portions">Ergibt 2 Portionen</span></p>
      </div>
    </div>
    <div class="brand-mark">Topfzauber</div>
  </section>

  <section class="label label--mushroom">
    <div class="label__tab"></div>
    <div class="label__band">
      <div class="label__art" role="img" aria-label="Aquarell-Illustration: Steinpilze, Beeren und Kräuter"></div>
      <svg class="label__panel" viewBox="0 0 368 275" aria-hidden="true">
        <path d="M96 0 C 96 150 175 255 292 275 L368 275 L368 0 Z"/>
      </svg>
      <div class="label__text">
        <h2 class="label__title">Pilzrahmsauce</h2>
        <p class="label__claim">VERSCHIEDENE EDELPILZE<br>UND FRISCHE SAHNE</p>
        <p class="label__amount"><span class="label__amount-key">Inhalt</span> <span class="label__amount-value">360g</span><span class="label__portions">Ergibt 2 Portionen</span></p>
      </div>
    </div>
    <div class="brand-mark">Topfzauber</div>
  </section>

  <section class="label label--chili">
    <div class="label__tab"></div>
    <div class="label__band">
      <div class="label__art" role="img" aria-label="Aquarell-Illustration: rote und grüne Chilischoten"></div>
      <svg class="label__panel" viewBox="0 0 368 275" aria-hidden="true">
        <path d="M96 0 C 96 150 175 255 292 275 L368 275 L368 0 Z"/>
      </svg>
      <div class="label__text">
        <h2 class="label__title">Chili <small>con</small> Carne</h2>
        <p class="label__claim label__claim--mixed">Kidney-Beans · Rindfleisch<br>und extra scharfes Chili</p>
        <p class="label__amount"><span class="label__amount-key">Inhalt</span> <span class="label__amount-value">360g</span><span class="label__portions">Ergibt 2 Portionen</span></p>
      </div>
    </div>
    <div class="brand-mark">Topfzauber</div>
  </section>

</main>
</body>
</html>
```